BRC Trifold

- Hello -
We are looking for an exciting trifold design for our residential roofing and interior remodeling company. Below is the website for more inspiration and images. We would like to include the Veteran Owned section somewhere on the back.

https://brellmontroofingandconstruction.com/

Thank You,
Wesley

```html
<!DOCTYPE html>
<html lang="en">
<head>
<meta charset="utf-8">
<title>Brellmont Roofing &amp; Construction Trifold</title>
<link rel="stylesheet" href="https://fonts.googleapis.com/css2?family=Montserrat:wght@600;700;800&family=Raleway:wght@400;500;600&display=swap">
<style>
:root{
  --maroon:#722f34;
  --taupe:#a0958d;
  --stage:#505050;
  --paper:#ffffff;
  --ink:#4a4a4a;
}
*{box-sizing:border-box;margin:0;padding:0}
html,body{width:1018px;height:1200px;overflow:hidden;background:var(--stage)}
body{position:relative;font-family:"Raleway",sans-serif;color:var(--ink)}
.sheet{position:absolute;left:160px;width:696px;height:493px;background:var(--paper);box-shadow:0 4px 14px rgba(0,0,0,.35)}
.sheet--outside{top:84px}
.sheet--inside{top:620px}
.panel{position:absolute;top:0;height:100%;overflow:hidden}
.panel--a{left:0;width:232px}
.panel--b{left:232px;width:232px}
.panel--c{left:464px;width:232px}
.panel--maroon{background:var(--maroon);color:#fff}
.photo{position:absolute}
.abs{position:absolute}

/* perks */
.perks-title{position:absolute;left:33px;top:31px;font-family:"Montserrat",sans-serif;font-weight:800;font-size:17.5px;line-height:18px;color:var(--maroon)}
.perks-list{position:absolute;left:33px;top:114px;width:185px;list-style:none;border-left:1px solid var(--maroon);margin-left:5px;padding-left:0}
.perks-list li{position:relative;padding-left:11px;font-size:8.6px;line-height:11px;color:var(--maroon);margin-bottom:11px}
.perks-list li:last-child{margin-bottom:0}
.perks-list svg{position:absolute;left:-5px;top:0}

/* contact */
.before-after{position:absolute;left:29px;width:174px;height:116px;border:2px solid #fff}
.before-after .tag{position:absolute;right:0;bottom:0;background:var(--maroon);color:#fff;font-family:"Montserrat",sans-serif;font-size:8px;font-weight:600;padding:1px 6px 1px 10px}
.contact{position:absolute;left:0;width:100%;text-align:center}
.contact-name{top:311px;font-family:"Montserrat",sans-serif;font-weight:700;font-size:10px}
.contact-addr{top:324px;font-size:10px;line-height:13.5px}
.contact-phone{top:357px;font-family:"Montserrat",sans-serif;font-weight:700;font-size:18px}
.contact-mail{top:379px;font-size:10px;font-style:italic}
.web-pill{position:absolute;left:31px;top:401px;width:166px;height:17px;border-radius:9px;background:#fff;color:#111;font-family:"Montserrat",sans-serif;font-weight:700;font-size:10px;letter-spacing:1.5px;text-align:center;line-height:17px}
.social{position:absolute;top:431px;left:0;width:100%;display:flex;justify-content:center;gap:3px}
.social span{width:16px;height:16px;border-radius:50%;background:#fff}

/* cover */
.brand{position:absolute;text-align:right;font-family:"Montserrat",sans-serif;font-weight:700;color:var(--maroon)}
.brand-name{font-size:14px;letter-spacing:2px;line-height:15px}
.brand-sub{font-size:7px;letter-spacing:3px;line-height:10px}
.brand-mark{display:inline-block;width:9px;height:9px;background:var(--maroon);margin-right:5px}
.intro{position:absolute;left:20px;top:319px;width:200px;font-size:8.6px;line-height:11px}
.services{position:absolute;top:361px;font-size:8.6px;line-height:11px}
.services h3{font-family:"Montserrat",sans-serif;font-weight:800;font-size:13px;line-height:13px;color:var(--maroon)}
.services h4{font-family:"Montserrat",sans-serif;font-weight:700;font-size:6px;color:var(--maroon);margin-bottom:2px}
.services li{list-style:none;white-space:nowrap}
.services li::before{content:"☑";color:var(--maroon);font-size:7px;margin-right:3px}
.phone-pill{position:absolute;background:var(--maroon);color:#fff;border-radius:12px;font-family:"Montserrat",sans-serif;font-weight:800;letter-spacing:2.4px;text-align:center}
.cover-web{position:absolute;left:19px;top:466px;width:190px;font-family:"Montserrat",sans-serif;font-weight:600;font-size:12px;letter-spacing:2.3px;color:var(--maroon);text-align:center}

/* inside */
.bar{position:absolute;left:0;width:100%;background:var(--maroon);color:#fff;font-family:"Montserrat",sans-serif;font-weight:700;font-size:12.5px;padding-left:17px;display:flex;align-items:center}
.body-copy{position:absolute;left:17px;width:200px;font-size:9.2px;line-height:12px;text-align:justify}
.body-copy b{color:#333}
.accent{position:absolute;font-family:"Raleway",sans-serif;font-weight:600;color:var(--maroon)}
.subhead{position:absolute;left:17px;font-weight:600;font-size:11.5px;color:var(--ink)}
.kitchen-copy{position:absolute;left:18px;top:56px;width:202px;color:#fff;font-size:9.2px;line-height:12px}
.quote-box{position:absolute;left:17px;top:348px;width:201px;height:83px;border:1px solid #fff}
.quote-text{position:absolute;left:0;top:374px;width:100%;text-align:center;color:#fff;font-size:10px;line-height:13px}
.quote-name{position:absolute;left:0;top:424px;width:100%;text-align:center;font-family:"Montserrat",sans-serif;font-weight:700;font-size:10px;color:var(--maroon)}
.quote-name span{background:var(--taupe);padding:0 2px}
.quote-web{position:absolute;left:0;top:457px;width:100%;text-align:center;font-size:13px;color:var(--maroon)}
.quote-web b{font-family:"Montserrat",sans-serif;font-weight:800}
</style>
</head>
<body>

<section class="sheet sheet--outside">
  <div class="panel panel--a">
    <h2 class="perks-title">PERKS THAT<br>COME FROM<br>WORKING WITH<br>PROFESSIONALS</h2>
    <ul class="perks-list">
      <li><svg width="10" height="10" viewBox="0 0 10 10"><circle cx="5" cy="5" r="5" fill="#722f34"/><path d="M2.6 5.2l1.6 1.5 3.2-3.3" stroke="#fff" stroke-width="1.3" fill="none"/></svg>Free Estimate</li>
      <li><svg width="10" height="10" viewBox="0 0 10 10"><circle cx="5" cy="5" r="5" fill="#722f34"/><path d="M2.6 5.2l1.6 1.5 3.2-3.3" stroke="#fff" stroke-width="1.3" fill="none"/></svg>Professional Interior<br>Design Consultation</li>
      <li><svg width="10" height="10" viewBox="0 0 10 10"><circle cx="5" cy="5" r="5" fill="#722f34"/><path d="M2.6 5.2l1.6 1.5 3.2-3.3" stroke="#fff" stroke-width="1.3" fill="none"/></svg>Insurance Inspections assistance<br>for an accurate assessment</li>
      <li><svg width="10" height="10" viewBox="0 0 10 10"><circle cx="5" cy="5" r="5" fill="#722f34"/><path d="M2.6 5.2l1.6 1.5 3.2-3.3" stroke="#fff" stroke-width="1.3" fill="none"/></svg>Insurance claim advocacy</li>
      <li><svg width="10" height="10" viewBox="0 0 10 10"><circle cx="5" cy="5" r="5" fill="#722f34"/><path d="M2.6 5.2l1.6 1.5 3.2-3.3" stroke="#fff" stroke-width="1.3" fill="none"/></svg>Once stop shop – General Contractor<br>to assist with all of your Restoration &amp;<br>Renovation needs</li>
      <li><svg width="10" height="10" viewBox="0 0 10 10"><circle cx="5" cy="5" r="5" fill="#722f34"/><path d="M2.6 5.2l1.6 1.5 3.2-3.3" stroke="#fff" stroke-width="1.3" fill="none"/></svg>Referral Bonus</li>
      <li><svg width="10" height="10" viewBox="0 0 10 10"><circle cx="5" cy="5" r="5" fill="#722f34"/><path d="M2.6 5.2l1.6 1.5 3.2-3.3" stroke="#fff" stroke-width="1.3" fill="none"/></svg>Military Discount</li>
      <li><svg width="10" height="10" viewBox="0 0 10 10"><circle cx="5" cy="5" r="5" fill="#722f34"/><path d="M2.6 5.2l1.6 1.5 3.2-3.3" stroke="#fff" stroke-width="1.3" fill="none"/></svg>Free Architectural Consultation</li>
    </ul>
    <svg class="abs" style="left:0;top:340px" width="232" height="153" viewBox="0 0 232 153">
      <polygon points="0,33 232,0 232,5 0,38" fill="#a0958d"/>
      <polygon points="0,42 232,9 232,153 0,153" fill="#b9916e" role="img" aria-label="Photo of a bright modern kitchen with a white island, wood cabinets and leather bar stools"/>
    </svg>
  </div>

  <div class="panel panel--b panel--maroon">
    <div class="before-after" style="top:31px">
      <div class="photo" style="inset:0;background:linear-gradient(#7ea9c9 0%,#5f8a3e 55%,#9a9a90 100%)" role="img" aria-label="Before photo of a brick ranch house with a garage and front lawn"></div>
      <span class="tag">BEFORE</span>
    </div>
    <div class="before-after" style="top:168px">
      <div class="photo" style="inset:0;background:linear-gradient(#7ea9c9 0%,#d9d2c6 45%,#5f8a3e 70%,#9a9a90 100%)" role="img" aria-label="After photo of the same house renovated with white walls and cedar siding"></div>
      <span class="tag">AFTER</span>
    </div>
    <div class="contact contact-name">Brellmont Roofing &amp; Construction</div>
    <div class="contact contact-addr">4410 Larkspur Avenue, Suite C<br>Oakmere, IL 60999</div>
    <div class="contact contact-phone"><svg width="13" height="13" viewBox="0 0 24 24" style="vertical-align:-1px"><path d="M6.6 10.8c1.4 2.8 3.8 5.1 6.6 6.6l2.2-2.2c.3-.3.7-.4 1-.2 1.1.4 2.3.6 3.6.6.6 0 1 .4 1 1V20c0 .6-.4 1-1 1C10.6 21 3 13.4 3 4c0-.6.4-1 1-1h3.5c.6 0 1 .4 1 1 0 1.3.2 2.5.6 3.6.1.3 0 .7-.2 1z" fill="none" stroke="#fff" stroke-width="1.6"/></svg>555-014-2870</div>
    <div class="contact contact-mail">brellmontroofing@mailhub.net</div>
    <div class="web-pill">WWW.BRELLMONT.COM</div>
    <div class="social"><span></span><span></span><span></span><span></span><span></span></div>
  </div>

  <div class="panel panel--c">
    <div class="brand" style="right:28px;top:50px">
      <div class="brand-name"><span class="brand-mark"></span>BRELLMONT</div>
      <div class="brand-sub">ROOFING &amp; CONSTRUCTION</div>
    </div>
    <svg class="abs" style="left:0;top:74px" width="232" height="230" viewBox="0 0 232 230">
      <polygon points="0,42 232,0 232,46 0,88" fill="#722f34"/>
      <polygon points="0,46 232,8 232,188 0,222" fill="#6f8a5a" role="img" aria-label="Photo of a white Tudor-style house with a grey shingle roof and green shrubs"/>
      <polygon points="0,216 232,176 232,182 0,226" fill="#a0958d"/>
    </svg>
    <p class="intro">Licensed &amp; accredited company with over 20 years&nbsp; construction experience in Residential &amp; Commercial Renovation &amp; Restoration.</p>
    <div class="services" style="left:21px">
      <h3>EXTERIOR</h3><h4>HOME REMODELING</h4>
      <ul><li>Roofing</li><li>Siding</li><li>Gutters</li><li>Soffit / Fascia</li></ul>
    </div>
    <div class="services" style="left:110px">
      <h3>INTERIOR</h3><h4>HOME REMODELING</h4>
      <ul><li>Home Improvement</li><li>Kitchen Remodeling</li><li>Bathroom Remodeling</li><li>Deck / Patio Build Ou</li></ul>
    </div>
    <div class="phone-pill" style="left:18px;top:442px;width:188px;height:22px;font-size:18px;line-height:22px">555-014-2870</div>
    <div class="cover-web">WWW.BRELLMONT.COM</div>
  </div>
</section>

<section class="sheet sheet--inside">
  <div class="panel panel--a">
    <div class="photo" style="left:0;top:0;width:232px;height:151px;background:linear-gradient(135deg,#5d8a3e,#3c4352 55%,#6e9a4a)" role="img" aria-label="Aerial photo of a house with a new dark shingle roof and green yard"></div>
    <div class="bar" style="top:151px;height:33px">ROOFING,SIDING &amp; GUTTER</div>
    <p class="body-copy" style="top:200px">Whether you’re looking to do roof repair, roof replacement, new gutters, new siding, trust our licensed professionals. We work with the top manufacturers in the industry <b>Crestline Summit Series Roofing System</b> – Gale Guard Shake, Summit Clear</p>
    <div class="accent" style="left:18px;top:279px;font-size:11.5px">Lifetime Warranty</div>
    <div class="bar" style="top:302px;height:33px">STORM DAMAG</div>
    <div class="subhead" style="top:349px">Renovation or Restoration</div>
    <p class="body-copy" style="top:364px">Time for new Roof, Siding or Gutters? Hail or Storm damage? We are here to assist in every aspect. With decades of experience negotiating with Insurance companies for accurate assessments, we work with the best trades for the project, and ensure your home is not only built well but looks just as beautiful.</p>
    <div class="phone-pill" style="left:18px;top:458px;width:193px;height:21px;font-size:18px;line-height:21px;letter-spacing:2px"><svg width="12" height="12" viewBox="0 0 24 24" style="vertical-align:-1px"><path d="M6.6 10.8c1.4 2.8 3.8 5.1 6.6 6.6l2.2-2.2c.3-.3.7-.4 1-.2 1.1.4 2.3.6 3.6.6.6 0 1 .4 1 1V20c0 .6-.4 1-1 1C10.6 21 3 13.4 3 4c0-.6.4-1 1-1h3.5c.6 0 1 .4 1 1 0 1.3.2 2.5.6 3.6.1.3 0 .7-.2 1z" fill="none" stroke="#fff" stroke-width="1.8"/></svg>555-014-2870</div>
  </div>

  <div class="panel panel--b" style="left:229px;width:235px;background:var(--taupe)">
    <div class="bar" style="top:0;height:33px;padding-left:18px">KITCHEN REMODELING</div>
    <p class="kitchen-copy">Your kitchen is the central hub of every home. We’ll collaborate with you to make this space open and functional for everyone to enjoy. We use the latest building products and trends to meet and exceed your expectations.</p>
    <div class="photo" style="left:0;top:151px;width:235px;height:184px;background:linear-gradient(160deg,#e9e6e1,#b9b3ab 55%,#6b5a4a)" role="img" aria-label="Photo of a white kitchen with a granite island, pendant lights and stainless steel appliances"></div>
    <div class="quote-box"></div>
    <svg class="abs" style="left:96px;top:323px" width="44" height="44" viewBox="0 0 44 44"><circle cx="22" cy="22" r="21" fill="#722f34"/><text x="22" y="38" text-anchor="middle" font-family="Montserrat,sans-serif" font-weight="800" font-size="34" fill="#fff">“</text></svg>
    <p class="quote-text">I wake up every day excited<br>to use my dream kitchen. Thank you,<br>Brellmont Roofing &amp; Construction!</p>
    <div class="quote-name"><span>- DANA WHITFIELD</span></div>
    <div class="quote-web">www.<b>BRELLMONT</b>.com</div>
  </div>

  <div class="panel panel--c">
    <div class="photo" style="left:0;top:0;width:232px;height:151px;background:linear-gradient(120deg,#c9ccd0,#eeeeec 50%,#d8d4cc)" role="img" aria-label="Photo of a marble bathroom with a glass shower, soaking tub and white vanity"></div>
    <div class="photo" style="left:0;top:151px;width:232px;height:150px;background:linear-gradient(120deg,#e6e4e0,#c9c0b4 55%,#5a4636)" role="img" aria-label="Photo of a modern bathroom with a freestanding tub, walk-in shower and dark wood vanity"></div>
    <div class="bar" style="top:301px;height:32px">BATHROOM REMODELING</div>
    <div class="subhead" style="top:343px">Make It Picture Perfect</div>
    <p class="body-copy" style="top:357px">Give your bathroom a new life and increase the value of your home at the same time. We offer full service design assistance to transform the bathroom into your very own spa retreat.</p>
    <div class="brand" style="right:28px;top:451px">
      <div class="brand-name"><span class="brand-mark"></span>BRELLMONT</div>
      <div class="brand-sub">ROOFING &amp; CONSTRUCTION</div>
    </div>
  </div>
</section>

</body>
</html>
```